Harborline Motors LLC

Car Dealer Customer Service
Address: 2741 Linden Avenue, Shelbyville, TN 37162
web: www.harborlinemotorstn.net
email: harborlinemotorstn@mailbox-example.net
Phone: (931) 555-0148
Phone: (629) 555-0173

```html
<!DOCTYPE html>
<html lang="en">
<head>
<meta charset="utf-8">
<title>Harborline Motors LLC – Business Card</title>
<link href="https://fonts.googleapis.com/css2?family=Poppins:wght@400;500;700&display=swap" rel="stylesheet">
<style>
  :root {
    --bg: #eceeed;
    --white: #ffffff;
    --amber: #edb446;
    --blue: #1f7cb5;
    --ink: #2a2a2a;
  }
  * { margin: 0; padding: 0; box-sizing: border-box; }
  html, body { width: 1067px; height: 1200px; overflow: hidden; }
  body {
    background: var(--bg);
    font-family: "Poppins", Arial, sans-serif;
    position: relative;
  }
  .card {
    position: absolute;
    left: 205px;
    width: 657px;
    height: 352px;
    overflow: hidden;
  }
  .card--front { top: 176px; background: var(--white); }
  .card--back { top: 653px; background: var(--amber); }

  .tab {
    position: absolute;
    left: 192px;
    width: 273px;
    height: 23px;
    background: var(--amber);
  }
  .tab--top { top: 0; border-radius: 0 0 10px 10px; }
  .tab--bottom { bottom: 0; border-radius: 10px 10px 0 0; }

  .brand-name {
    position: absolute;
    font-weight: 700;
    text-transform: uppercase;
    white-space: nowrap;
    letter-spacing: 0.3px;
  }
  .card--front .brand-name {
    left: 0; right: 0; top: 160px;
    text-align: center;
    font-size: 23px;
    color: var(--blue);
  }
  .card--back .brand-name {
    left: 24px; width: 182px; top: 200px;
    text-align: center;
    font-size: 15px;
    color: var(--ink);
  }

  .notch {
    position: absolute;
    top: 80px;
    width: 23px;
    height: 192px;
    background: var(--white);
  }
  .notch--left { left: 0; border-radius: 0 8px 8px 0; }
  .notch--right { right: 0; border-radius: 8px 0 0 8px; }

  .divider {
    position: absolute;
    left: 211px; top: 78px;
    width: 2px; height: 192px;
    background: var(--white);
  }

  .role-title {
    position: absolute;
    left: 232px; top: 76px;
    font-size: 20.5px;
    font-weight: 500;
    color: var(--ink);
    text-transform: uppercase;
    border-bottom: 1.5px solid var(--ink);
    line-height: 1.2;
    white-space: nowrap;
  }

  .contact-list { list-style: none; }
  .contact-item {
    position: absolute;
    left: 238px;
    display: flex;
    align-items: flex-start;
    font-size: 16.5px;
    color: var(--ink);
    line-height: 26px;
    white-space: nowrap;
  }
  .contact-icon { width: 14px; height: 14px; margin-top: 5px; margin-right: 17px; flex: none; }
  .contact-item--phone { top: 128px; }
  .contact-item--email { top: 186px; }
  .contact-item--web { top: 217px; }
  .contact-item--address { top: 250px; }
</style>
</head>
<body>

<section class="card card--front">
  <div class="tab tab--top"></div>
  <div class="brand-name">Harborline Motors</div>
  <div class="tab tab--bottom"></div>
</section>

<section class="card card--back">
  <div class="notch notch--left"></div>
  <div class="notch notch--right"></div>

  <div class="brand-name">Harborline Motors</div>
  <div class="divider"></div>

  <h1 class="role-title">Car Dealer Customer Service</h1>

  <ul class="contact-list">
    <li class="contact-item contact-item--phone">
      <svg class="contact-icon" viewBox="0 0 24 24" aria-hidden="true"><path d="M6.6 10.8a15 15 0 0 0 6.6 6.6l2.2-2.2a1 1 0 0 1 1-.25 11.4 11.4 0 0 0 3.6.6 1 1 0 0 1 1 1V20a1 1 0 0 1-1 1A17 17 0 0 1 3 4a1 1 0 0 1 1-1h3.5a1 1 0 0 1 1 1c0 1.25.2 2.45.6 3.6a1 1 0 0 1-.25 1z" fill="none" stroke="#2a2a2a" stroke-width="2"/></svg>
      <span>(931) 555-0148<br>(629) 555-0173</span>
    </li>
    <li class="contact-item contact-item--email">
      <svg class="contact-icon" viewBox="0 0 24 24" aria-hidden="true"><rect x="2" y="6" width="20" height="13" fill="#2a2a2a"/><path d="M2 6l10 7 10-7" fill="none" stroke="#edb446" stroke-width="1.6"/></svg>
      <span>harborlinemotorstn@mailbox-example.net</span>
    </li>
    <li class="contact-item contact-item--web">
      <svg class="contact-icon" viewBox="0 0 24 24" aria-hidden="true"><g fill="none" stroke="#2a2a2a" stroke-width="1.8"><circle cx="12" cy="12" r="10"/><ellipse cx="12" cy="12" rx="4.5" ry="10"/><path d="M2 12h20M4 6.5h16M4 17.5h16"/></g></svg>
      <span>www.harborlinemotorstn.net</span>
    </li>
    <li class="contact-item contact-item--address">
      <svg class="contact-icon" viewBox="0 0 24 24" aria-hidden="true"><g fill="none" stroke="#2a2a2a" stroke-width="2"><path d="M12 17s-6-6-6-10a6 6 0 0 1 12 0c0 4-6 10-6 10z"/><circle cx="12" cy="7" r="2"/><path d="M6 17l-3 5h18l-3-5"/></g></svg>
      <span>2741 Linden Avenue, Shelbyville, TN 37162</span>
    </li>
  </ul>
</section>

</body>
</html>
```